Design for a 3-4 screens mobile app

The app is a "simple" ordering mobile app.
1. START screen : user can select either "NEW order" either "VIEW history" - or, can access the usual Contact, About, and Conditions pages.
2. NEW order : is a sequence of 3 basic screens/forms made of 3-4 fields each. Logic is the following: you select the service you need, its recurrence, mention where you are located and then you post it towards the marketplace...
3. VIEW history : is where you land at the end of the ordering process - and accessible from START screen. You see there your previous orders, and their statuses.
Mandatory : we need design for START screen, NEW order and VIEW history screens.
Design but be optimized for Smartphones, used in Portrait mode.
Please take into account the design of the website promoting the Mobile App: https://tidyvanlane.be/
Optional but of course nice to have if you could propose some design or guidance for Contact, About, and Conditions pages...
Here attached a full screen sequence.
Updates
Thanks for all your proposals ! They were submitted to the final customer, he selects one ASAP !
Number of Pages Required
3 page
Look and feel
Each slider illustrates characteristics of the customer's brand and the style your logo design should communicate.

```html
<!DOCTYPE html>
<html lang="en">
<head>
<meta charset="utf-8">
<title>Tidy Van Lane – Menu</title>
<link href="https://fonts.googleapis.com/css2?family=Montserrat:wght@400;700&display=swap" rel="stylesheet">
<style>
  :root{
    --orange:#f26a12;
    --orange-soft:#f7a35f;
    --white:#ffffff;
    --ink:#111111;
    --menu-grey:#6f6f6f;
    --frame-grey:#8a8a8a;
    --bar-top:#f4f4f4;
    --bar-bottom:#d9d9d9;
    --teal:#52b9c4;
    --blue:#6aa7d8;
    --blush:#f2a57d;
    --art:#e7b27a;
    --veil:rgba(255,255,255,0.92);
  }
  *{box-sizing:border-box;margin:0;padding:0}
  html,body{width:675px;height:1200px;overflow:hidden;background:var(--white)}
  body{font-family:"Montserrat",Arial,sans-serif;position:relative}
  .screen{position:relative;width:675px;height:1200px;overflow:hidden;background:var(--white)}

  .status-bar{position:absolute;top:0;left:0;width:675px;height:45px;
    background:linear-gradient(var(--bar-top),var(--bar-bottom));
    color:var(--ink);font-family:"Helvetica Neue",Arial,sans-serif;font-size:22px}
  .status-bar .carrier{position:absolute;left:12px;top:10px;display:flex;align-items:center;gap:8px}
  .status-bar .signal{display:flex;gap:3px;align-items:flex-end}
  .status-bar .signal i{display:block;width:5px;background:var(--ink)}
  .status-bar .clock{position:absolute;left:0;right:0;top:10px;text-align:center}

  .app-header{position:absolute;top:45px;left:0;width:675px;height:63px;background:var(--orange);
    display:flex;align-items:center}
  .brand{display:flex;align-items:center;gap:12px;margin-left:66px;color:var(--white);
    font-weight:700;font-size:21px;letter-spacing:.5px}
  .brand-square{width:52px;height:52px;background:var(--orange-soft)}
  .close-btn{position:absolute;right:30px;top:14px;width:36px;height:36px}

  .home-content{position:absolute;top:108px;left:0;width:675px;height:1092px}
  .intro-title{position:absolute;top:44px;width:100%;text-align:center;color:var(--orange);
    font-weight:700;font-size:32px}
  .intro-sub{position:absolute;top:84px;left:90px;width:495px;text-align:center;color:#555;font-size:19px;line-height:24px}
  .intro-copy{position:absolute;top:270px;left:80px;width:330px;color:#555;font-size:19px;line-height:28px}
  .intro-art{position:absolute;left:460px;top:150px;width:140px;height:260px;border-radius:60px 60px 20px 20px;
    background:linear-gradient(var(--art),#f3d7b6)}
  .action{position:absolute;left:0;width:675px;color:var(--white);font-weight:700;font-size:46px;line-height:56px}
  .action span{position:absolute;left:153px}
  .action svg{position:absolute;left:434px}
  .action-order{top:511px;height:236px;background:var(--teal)}
  .action-order span{top:62px}
  .action-order svg{top:84px}
  .action-history{top:758px;height:236px;background:var(--blue)}
  .action-history span{top:72px}
  .action-history svg{top:70px}
  .footer-band{position:absolute;top:994px;left:0;width:675px;height:98px;background:var(--blush)}

  .menu-overlay{position:absolute;top:108px;left:0;width:675px;height:1092px;background:var(--veil)}
  .menu{list-style:none}
  .menu li{position:absolute;left:0;width:675px;text-align:center;color:var(--menu-grey);
    font-size:44px;line-height:56px;letter-spacing:.5px}
  .menu .item-home{top:164px}
  .menu .item-home a{display:inline-block;width:262px;height:102px;line-height:98px;border:2px solid var(--frame-grey)}
  .menu .item-about{top:354px}
  .menu .item-contact{top:525px}
  .menu .item-terms{top:694px}
  .menu a{color:inherit;text-decoration:none}
</style>
</head>
<body>
<div class="screen">
  <div class="status-bar">
    <div class="carrier">
      <div class="signal"><i style="height:6px"></i><i style="height:9px"></i><i style="height:12px"></i><i style="height:15px"></i><i style="height:18px"></i></div>
      <span>CARRIER 3G</span>
    </div>
    <div class="clock">12:00</div>
  </div>

  <header class="app-header">
    <div class="brand"><div class="brand-square"></div><span>TIDY VAN LANE</span></div>
    <svg class="close-btn" viewBox="0 0 36 36" aria-label="Close menu"><path d="M5 5 L31 31 M31 5 L5 31" stroke="#fff" stroke-width="6" stroke-linecap="round"/></svg>
  </header>

  <main class="home-content" aria-hidden="true">
    <h1 class="intro-title">TIDY VAN LANE</h1>
    <p class="intro-sub">Book your home services in a few taps, simple and fast every day</p>
    <p class="intro-copy">Choose a service, set the rhythm and we do the rest</p>
    <div class="intro-art" role="img" aria-label="Illustration of a cleaning helper"></div>
    <div class="action action-order">
      <span>MAKE AN<br>ORDER</span>
      <svg width="88" height="80" viewBox="0 0 88 80"><rect x="0" y="0" width="38" height="34" fill="#fff"/><rect x="0" y="44" width="38" height="34" fill="#fff"/><rect x="48" y="44" width="38" height="34" fill="#fff"/><path d="M67 2 V32 M52 17 H82" stroke="#fff" stroke-width="8"/></svg>
    </div>
    <div class="action action-history">
      <span>VIEW<br>HISTORY</span>
      <svg width="80" height="96" viewBox="0 0 80 96"><rect x="6" y="10" width="56" height="80" rx="6" fill="none" stroke="#fff" stroke-width="7"/><rect x="20" y="4" width="28" height="14" fill="#fff"/><path d="M18 40 H50 M18 56 H50 M18 72 H40" stroke="#fff" stroke-width="6"/><path d="M74 20 L46 62" stroke="#fff" stroke-width="8"/></svg>
    </div>
    <div class="footer-band"></div>
  </main>

  <nav class="menu-overlay">
    <ul class="menu">
      <li class="item-home"><a href="#">HOME</a></li>
      <li class="item-about"><a href="#">ABOUT</a></li>
      <li class="item-contact"><a href="#">CONTACT</a></li>
      <li class="item-terms"><a href="#">TERMS OF USE</a></li>
    </ul>
  </nav>
</div>
</body>
</html>
```